Cosmetics Brand Logo and Bottle Label Design

We are creating a new cosmetics brand called "Milo Tennant" and would like you to create an amazing logo and bottle label for this brand's new 100% pure argan oil product.
For the logo, we really like the logo's of Vanra Okell and Ruvi. The text should be Sans Serif (without feet).
For the actual bottle label, please find attached labels of one of our competitors design which really like. We really like the simplicity and elegance of the design. The only difference is that our product will be using light turqoise as the brand color. Please feel free to add your own creativity into it as well.
Industry/Entity Type
Cosmetics
Logo Text
Milo Tennant
Font styles to use

```html
<!DOCTYPE html>
<html lang="en">
<head>
<meta charset="utf-8">
<title>Milo Tennant – Argan Oil Label</title>
<link rel="stylesheet" href="https://fonts.googleapis.com/css2?family=Raleway:wght@200&family=Encode+Sans+Condensed:wght@300&family=Roboto+Slab:wght@200&display=swap">
<style>
  :root {
    --backdrop: #e4e6e9;
    --label-mint: #e2fddc;
    --brand-turquoise: #2f9a70;
    --brand-edge: #1f5a3e;
    --brand-ink: #e2fddc;
    --detail-grey: #c3cfbf;
    --product-ink: #111111;
  }
  html, body {
    margin: 0;
    padding: 0;
    width: 1200px;
    height: 2215px;
    overflow: hidden;
    background: var(--backdrop);
  }
  .canvas {
    position: relative;
    width: 1200px;
    height: 2215px;
  }
  .label {
    position: absolute;
    left: 100px;
    top: 549px;
    width: 1000px;
    height: 1117px;
    display: block;
  }
  .label-ground { fill: var(--label-mint); }
  .brand-band { fill: var(--brand-turquoise); }
  .brand-band-edge { fill: var(--brand-edge); }
  .brand-name {
    font-family: "Raleway", sans-serif;
    font-weight: 200;
    font-size: 132px;
    fill: var(--brand-ink);
  }
  .product-detail {
    font-family: "Encode Sans Condensed", sans-serif;
    font-weight: 300;
    font-size: 54px;
    letter-spacing: -1px;
    fill: var(--detail-grey);
  }
  .product-name {
    font-family: "Roboto Slab", serif;
    font-weight: 200;
    font-size: 222px;
    fill: var(--product-ink);
  }
</style>
</head>
<body>
<main class="canvas">
  <svg class="label" viewBox="0 0 1000 1117" xmlns="http://www.w3.org/2000/svg" aria-label="Milo Tennant argan oil label">
    <rect class="label-ground" x="0" y="0" width="1000" height="1117"/>
    <rect class="brand-band" x="106" y="0" width="217" height="975"/>
    <rect class="brand-band-edge" x="106" y="0" width="217" height="6"/>
    <text class="brand-name" transform="translate(262 921) rotate(-90)">Milo Tennant</text>
    <text class="product-detail" x="398" y="570">100% PURE ORIGINAL</text>
    <text class="product-detail" x="398" y="660">ARGAN OIL</text>
    <text class="product-name" x="392" y="911">light</text>
  </svg>
</main>
</body>
</html>
```